The name of the company is Torvend Holdings, LLC. I would like a business card with a logo.

On the top left, I would like a logo design of a crown and I would like Torvend over the top of the crown while Holdings on the bottom. Please see attached files as an example of crown and positioning of Torvend Holdings. Then I would like the letters TH in the middle(see picture).

Colors

Designer to choose colors to be used in the design.

```html
<!DOCTYPE html>
<html lang="en">
<head>
<meta charset="utf-8">
<title>Torvend Holdings – Business Card</title>
<link href="https://fonts.googleapis.com/css2?family=Cinzel:wght@400;600&family=Lato:wght@400&display=swap" rel="stylesheet">
<style>
  :root {
    --backdrop: #2e2e2c;
    --card-black: #111111;
    --card-white: #f7f7f5;
    --ink: #1a1a1a;
    --silver: #8d8d8d;
    --white: #ffffff;
  }
  * { margin: 0; padding: 0; box-sizing: border-box; }
  html, body {
    width: 1200px; height: 824px; overflow: hidden;
    background: var(--backdrop);
  }
  .canvas { position: relative; width: 1200px; height: 824px; }

  .card {
    position: absolute; width: 500px; height: 286px;
    border-radius: 3px;
    box-shadow: 0 10px 28px rgba(0,0,0,0.45);
  }
  .card-back { left: 70px; top: 90px; background: var(--card-black); }
  .card-front { left: 630px; top: 90px; background: var(--card-white); color: var(--ink); }

  .wordmark {
    position: absolute; text-align: center;
    font-family: 'Cinzel', serif; font-weight: 400;
    line-height: 1;
  }
  .wordmark .mark-dot {
    display: block; margin: 0 auto 14px;
    border-radius: 50%;
  }
  .wordmark .mark-name { display: block; }
  .wordmark .mark-sub { display: block; }

  .card-back .wordmark { left: 0; right: 0; top: 78px; color: var(--silver); }
  .card-back .mark-dot { width: 34px; height: 34px; border: 2px solid var(--silver); }
  .card-back .mark-name { font-size: 50px; letter-spacing: 4px; }
  .card-back .mark-sub { font-size: 13px; letter-spacing: 8px; margin-top: 8px; }

  .card-front .wordmark { left: 26px; top: 26px; width: 150px; color: var(--ink); }
  .card-front .mark-dot { width: 18px; height: 18px; border: 1.5px solid var(--ink); margin-bottom: 8px; }
  .card-front .mark-name { font-size: 27px; letter-spacing: 2px; }
  .card-front .mark-sub { font-size: 7px; letter-spacing: 4px; margin-top: 4px; }

  .contact-list {
    position: absolute; left: 28px; top: 118px;
    list-style: none;
    font-family: 'Lato', sans-serif; font-size: 11.5px; line-height: 17px;
  }
  .contact-list li { display: flex; align-items: flex-start; gap: 6px; }
  .contact-list svg { width: 9px; height: 9px; margin-top: 4px; flex: none; fill: var(--ink); }
  .contact-list .indent { padding-left: 15px; }

  .holder {
    position: absolute; right: 28px; top: 44px; text-align: right;
    font-family: 'Cinzel', serif; font-weight: 600; font-size: 15px;
    line-height: 21px; letter-spacing: 0.5px;
  }

  .logo-lockup { left: 70px; top: 560px; width: 290px; color: var(--white); }
  .logo-lockup .mark-dot { width: 48px; height: 48px; border: 2px solid var(--white); }
  .logo-lockup .mark-name { font-size: 54px; letter-spacing: 4px; }
  .logo-lockup .mark-sub { font-size: 14px; letter-spacing: 8px; margin-top: 10px; }
</style>
</head>
<body>
<main class="canvas">

  <section class="card card-back" aria-label="Card back">
    <div class="wordmark">
      <span class="mark-dot"></span>
      <span class="mark-name">TORVEND</span>
      <span class="mark-sub">HOLDINGS</span>
    </div>
  </section>

  <section class="card card-front" aria-label="Card front">
    <div class="wordmark">
      <span class="mark-dot"></span>
      <span class="mark-name">TORVEND</span>
      <span class="mark-sub">HOLDINGS</span>
    </div>

    <ul class="contact-list">
      <li>
        <svg viewBox="0 0 10 10" aria-hidden="true"><path d="M5 0a3.5 3.5 0 0 0-3.5 3.5C1.5 6 5 10 5 10s3.5-4 3.5-6.5A3.5 3.5 0 0 0 5 0zm0 5a1.4 1.4 0 1 1 0-2.8A1.4 1.4 0 0 1 5 5z"/></svg>
        <span>Torvend Holdings, LLC</span>
      </li>
      <li class="indent">418 Harbor Crest Lane, Suite 300</li>
      <li class="indent">Fairmont Ridge, CA 90511</li>
      <li>
        <svg viewBox="0 0 10 10" aria-hidden="true"><path d="M2 0.5l1.8 2.2-1 1.1c.6 1.3 1.5 2.2 2.8 2.8l1.1-1L9 7.4 8 9.4C4.3 9.2.8 5.7.6 2z"/></svg>
        <span>(310) 555-0148</span>
      </li>
      <li>
        <svg viewBox="0 0 10 10" aria-hidden="true"><path d="M0 2h10v6H0z M0.6 2.4L5 5.6 9.4 2.4" fill="none" stroke="#1a1a1a" stroke-width="1"/></svg>
        <span>n.torvend.holdings@mailbox.com</span>
      </li>
    </ul>

    <div class="holder">
      <div>Navid Soren Torvend, MBA</div>
      <div>Founder/CEO</div>
    </div>
  </section>

  <div class="wordmark logo-lockup" aria-label="Torvend Holdings logo">
    <span class="mark-dot"></span>
    <span class="mark-name">TORVEND</span>
    <span class="mark-sub">HOLDINGS</span>
  </div>

</main>
</body>
</html>
```